Keystone Ridge Construction LLC

We need a professional and colorful website that describes our company [please see below]:

CORE COMPETENCIES

About Us: Keystone Ridge Construction, LLC is a veteran-owned business, and is a leading force in the construction industry. We have continuously provided exceptional services to our clients. With a wealth of experience and a commitment of excellence, we have earned a reputation for delivering high-quality projects on time and within budget.

Core Competencies:

Experience: With decades of experience, we bring unparalleled expertise to every project we undertake. Our team consists of seasoned professionals who are experts in their respective fields.

Portfolio: Our portfolio encompasses a wide range of construction projects, including commercial building, industrial facilities, infrastructure development and more.

Innovation: We stay at the forefront of industry trends and technologies, leveraging the latest tools and techniques to deliver innovative solutions.

Client Satisfaction: Our commitment to client satisfaction is unwavering. We prioritize open communication, transparency, and responsiveness, working closely with clients to understand their needs and deliver results.

Safety: Safety is our top priority on every job site. We adhere to the highest safety standards and implement rigorous safety protocols to ensure the well-being of our workers and stakeholders.

KEY SERVICES

General Contracting
Construction Management
Design-Build Services
Pre-construction Planning
Value Engineering
Sustainable Construction Practices
Renovation and Remodeling
Quality Assurance and Control
Project Estimating and Budgeting
Permitting and Regulatory Compliance

CONTACT INFORMATION

Douglas Whitfield, President
Email Address [TBD]
Website Address [TBD]
555.214.6093

Federal Government and Commercial Agencies

Construction and Design Build

• Please use our attached logo and color scheme that was designed through Pixel Forum. Please include the Nation's Capitol building with a patriotic feel and include a diverse work force. Include federal buildings in the pictures. Please include in the opeing tagline that the company is Veteran Owned.

```html
<!DOCTYPE html>
<html lang="en">
<head>
<meta charset="utf-8">
<title>Keystone Ridge Construction LLC</title>
<link rel="stylesheet" href="https://fonts.googleapis.com/css2?family=Cinzel:wght@500;600&family=Poppins:wght@400;500;600;700&display=swap">
<style>
:root{
  --navy:#232a65;
  --green:#8dc63f;
  --white:#ffffff;
  --ink:#2b2b2b;
  --muted:#555a66;
  --dark:#1d1d1f;
  --card-shadow:0 4px 14px rgba(0,0,0,.12);
}
*{box-sizing:border-box;margin:0;padding:0}
html,body{width:1200px;height:4747px;overflow:hidden}
body{font-family:"Poppins",sans-serif;color:var(--ink);background:var(--white);position:relative}
.abs{position:absolute}

/* header */
.site-header{left:0;top:0;width:1200px;height:92px;background:var(--white);border-top:4px solid var(--navy);z-index:5}
.brand{left:112px;top:24px;display:flex;align-items:center;gap:10px}
.brand-mark{width:22px;height:22px;background:var(--green)}
.brand-name{font-family:"Cinzel",serif;font-weight:600;font-size:17px;color:var(--navy);line-height:1.1;width:190px}
.nav{left:383px;top:36px;display:flex;gap:30px;font-size:15px;font-weight:500;color:var(--ink)}
.nav .active{color:var(--navy);font-weight:600}
.btn{display:inline-block;background:var(--green);color:var(--white);font-weight:600;font-size:13px;letter-spacing:.5px;text-align:center;border-radius:2px}
.header-cta{left:741px;top:27px;width:145px;height:46px;line-height:46px}
.call-icon{left:914px;top:24px;width:44px;height:44px;border-radius:50%;background:var(--navy)}
.call-label{left:970px;top:24px;font-size:12px;color:var(--navy);font-weight:500}
.call-number{left:970px;top:42px;font-size:22px;font-weight:700;color:var(--navy)}

/* hero */
.hero{left:0;top:92px;width:1200px;height:713px;background:linear-gradient(180deg,#e9a98b 0%,#d79a8a 25%,#7d6f72 55%,#4f5a3e 80%,#3e4a31 100%)}
.hero-title{left:0;top:170px;width:1200px;text-align:center;color:var(--navy)}
.hero-title .line1{font-family:"Cinzel",serif;font-weight:600;font-size:54px;line-height:1}
.hero-title .line2{font-family:"Cinzel",serif;font-weight:500;font-size:31px;margin-top:6px}
.hero-cta{left:527px;top:306px;width:146px;height:44px;line-height:44px}
.dots{display:flex;gap:8px;align-items:center}
.dot{width:11px;height:11px;border-radius:50%;border:1.5px solid var(--white)}
.dot.on{background:var(--green);border-color:var(--green);width:15px;height:15px}
.hero-dots{left:567px;top:680px}
.hero-curve{left:0;top:645px;width:1200px;height:160px}

/* section headings */
.heading{font-family:"Cinzel",serif;font-weight:600;font-size:40px;color:var(--navy);text-align:center;width:1200px;left:0}
.underline{width:48px;height:4px;background:var(--green)}

/* about */
.about-accent{left:410px;top:905px;width:205px;height:150px;background:var(--green)}
.about-photo{left:143px;top:928px;width:447px;height:427px;background:linear-gradient(160deg,#cfd6dc 0%,#eaeaea 40%,#9a8b76 65%,#5f7a45 100%)}
.about-dots{left:95px;top:1185px;width:330px;height:215px}
.about-title{left:638px;top:948px;font-family:"Cinzel",serif;font-weight:600;font-size:40px;color:var(--navy)}
.about-underline{left:638px;top:1003px}
.about-text{left:638px;top:1030px;width:452px;font-size:16px;line-height:27px;color:#333;text-align:justify}
.about-cta{left:638px;top:1257px;width:147px;height:46px;line-height:46px}

/* services */
.services-curve{left:0;top:1505px;width:1200px;height:180px}
.services{left:0;top:1684px;width:1200px;height:766px;background:var(--green)}
.services-title{top:1740px}
.services-underline{left:576px;top:1797px;background:var(--navy)}
.service-card{width:218px;height:198px;background:var(--white);border-radius:6px;box-shadow:var(--card-shadow);text-align:center}
.service-card svg{display:block;margin:20px auto 0;width:88px;height:100px}
.service-card .label{font-size:17px;font-weight:600;line-height:23px;color:var(--navy);margin-top:10px;padding:0 6px}
.service-card.featured{background:var(--navy)}
.service-card.featured .label{color:var(--white)}
.view-all{left:527px;top:2282px;width:146px;height:46px;line-height:46px;background:var(--navy)}

/* experience */
.experience{left:0;top:2450px;width:1200px;height:267px;background:var(--navy);text-align:center;color:var(--white)}
.experience h2{font-family:"Cinzel",serif;font-weight:600;font-size:38px;margin-top:68px}
.experience .underline{margin:8px auto 0}
.experience p{font-size:16px;line-height:27px;width:820px;margin:22px auto 0}

/* portfolio */
.portfolio-title{top:2790px}
.portfolio-underline{left:576px;top:2844px}
.shot{background:linear-gradient(180deg,#a9c6e6 0%,#c7d4de 40%,#7c8797 62%,#4f7a3a 100%)}
.shot.modern{background:linear-gradient(180deg,#8fb0d8 0%,#e8e8e8 45%,#8a6a4a 65%,#5a7d3d 100%)}
.arrow-btn{width:54px;height:54px;border-radius:50%;border:2px solid var(--navy)}

/* testimonials */
.reviews-title{top:3606px}
.reviews-underline{left:576px;top:3663px}
.review{width:264px;border:1px solid #dcdcdc;background:var(--white);padding:22px 16px}
.stars{display:flex;gap:5px}
.review h3{font-size:17px;font-weight:600;line-height:24px;color:var(--navy);margin-top:18px}
.review p{font-size:14px;line-height:23px;color:#444;margin-top:12px}
.reviewer{display:flex;align-items:center;gap:10px;margin-top:18px}
.avatar{width:38px;height:38px;border-radius:50%;background:#c9ced8}
.reviewer b{display:block;font-size:15px;color:var(--navy);font-weight:600}
.reviewer span{font-size:12px;color:#555}
.review-dots{left:562px;top:4130px}
.review-dots .dot{border-color:#999}
.review-dots .dot.on{background:#d0312d;border-color:#d0312d}

/* footer */
.footer-curve{left:0;top:4175px;width:1200px;height:140px}
.site-footer{left:0;top:4314px;width:1200px;height:433px;background:var(--dark)}
.footer-brand{left:190px;top:4462px;width:200px;text-align:center;font-family:"Cinzel",serif;font-weight:600;font-size:19px;line-height:1.25;color:var(--white)}
.social{top:4545px;width:34px;height:34px;border-radius:50%;border:1.5px solid var(--white)}
.footer-col{color:var(--white)}
.footer-col h4{font-size:20px;font-weight:600;color:var(--white)}
.footer-col .underline{width:40px;height:3px;margin:8px 0 14px}
.footer-col a{display:block;color:var(--white);text-decoration:none;font-size:13px;line-height:26px}
.footer-rule{left:110px;top:4662px;width:980px;height:1px;background:var(--green)}
.copyright{left:115px;top:4680px;font-size:13px;color:var(--white)}
.legal{left:862px;top:4680px;font-size:13px;display:flex;gap:22px;color:var(--white)}
</style>
</head>
<body>

<!-- header -->
<header class="site-header abs">
  <div class="brand abs"><span class="brand-mark"></span><span class="brand-name">Keystone Ridge Construction LLC</span></div>
  <nav class="nav abs"><span class="active">→ Home ←</span><span>About</span><span>Services</span><span>Projects</span></nav>
  <a class="btn header-cta abs">CONTACT US</a>
  <div class="call-icon abs">
    <svg width="44" height="44" viewBox="0 0 44 44"><path d="M16 13c1-1 2-1 3 0l2 3c.6 1 .4 2-.4 2.8l-1.3 1.1c1 2.3 2.7 4 5 5l1.1-1.3c.8-.8 1.8-1 2.8-.4l3 2c1 1 1 2 0 3l-1.6 1.6c-1.3 1.3-3.4 1.4-5.3.5-4.6-2.2-8-5.6-10.2-10.2-.9-1.9-.8-4 .5-5.3z" fill="#fff"/></svg>
  </div>
  <div class="call-label abs">Call Us Today!</div>
  <div class="call-number abs">+1 555 214 6093</div>
</header>

<!-- hero -->
<section class="hero abs" role="img" aria-label="Two-storey family home with a lit porch and lawn at sunset"></section>
<div class="hero-title abs">
  <div class="line1">Keystone Ridge</div>
  <div class="line2">Construction LLC</div>
</div>
<a class="btn hero-cta abs">GET STARTED</a>
<svg class="hero-curve abs" viewBox="0 0 1200 160" preserveAspectRatio="none">
  <path d="M0 160 Q600 -124 1200 160Z" fill="#232a65"/>
  <path d="M0 160 Q600 -60 1200 160Z" fill="#fff"/>
</svg>
<div class="dots hero-dots abs"><span class="dot"></span><span class="dot on"></span><span class="dot"></span><span class="dot"></span></div>

<!-- about -->
<div class="about-accent abs"></div>
<svg class="about-dots abs" viewBox="0 0 330 215">
  <defs><pattern id="dotgrid" width="19" height="19" patternUnits="userSpaceOnUse"><circle cx="3" cy="3" r="2.6" fill="#111"/></pattern></defs>
  <rect x="0" y="0" width="50" height="215" fill="url(#dotgrid)"/>
  <rect x="0" y="165" width="330" height="50" fill="url(#dotgrid)"/>
</svg>
<div class="about-photo abs" role="img" aria-label="Modern white and timber-clad house with landscaped front garden"></div>
<h2 class="about-title abs">About Us</h2>
<div class="underline about-underline abs"></div>
<p class="about-text abs">Keystone Ridge Construction, LLC [KRC LLC] is a veteran-owned business, and is a leading force in the construction industry. We have continuously provided exceptional services to our clients. With a wealth of experience and a commitment of excellence, we have earned a reputation for delivering high-quality projects on time and within budget.</p>
<a class="btn about-cta abs">LEARN MORE</a>

<!-- services -->
<svg class="services-curve abs" viewBox="0 0 1200 180" preserveAspectRatio="none">
  <path d="M0 0 Q600 270 1200 0 V180 H0Z" fill="#232a65"/>
  <path d="M0 14 Q600 300 1200 14 V180 H0Z" fill="#8dc63f"/>
</svg>
<section class="services abs"></section>
<h2 class="heading services-title abs">Our Services</h2>
<div class="underline services-underline abs"></div>

<svg width="0" height="0" style="position:absolute">
  <defs>
    <symbol id="hex" viewBox="0 0 88 100"><path d="M44 2 84 25 84 75 44 98 4 75 4 25Z" fill="#232a65" stroke="#dfe3ee" stroke-width="3"/></symbol>
  </defs>
</svg>

<div class="service-card abs" style="left:114px;top:1848px">
  <svg viewBox="0 0 88 100"><use href="#hex"/><rect x="30" y="32" width="26" height="34" rx="2" fill="none" stroke="#fff" stroke-width="2.5"/><path d="M35 42h16M35 49h16M35 56h10" stroke="#fff" stroke-width="2.5"/></svg>
  <div class="label">General<br>Contracting</div>
</div>
<div class="service-card abs" style="left:364px;top:1848px">
  <svg viewBox="0 0 88 100"><use href="#hex"/><circle cx="44" cy="44" r="7" fill="none" stroke="#fff" stroke-width="2.5"/><path d="M30 66c2-9 8-12 14-12s12 3 14 12" fill="none" stroke="#fff" stroke-width="2.5"/><circle cx="44" cy="50" r="20" fill="none" stroke="#fff" stroke-width="2" stroke-dasharray="5 4"/></svg>
  <div class="label">Construction<br>Management</div>
</div>
<div class="service-card featured abs" style="left:614px;top:1848px">
  <svg viewBox="0 0 88 100"><path d="M44 2 84 25 84 75 44 98 4 75 4 25Z" fill="#fff"/><rect x="30" y="34" width="28" height="30" fill="none" stroke="#232a65" stroke-width="2.5"/><path d="M36 58 52 40M48 40h4v4" fill="none" stroke="#232a65" stroke-width="2.5"/></svg>
  <div class="label">Design-Build<br>Services</div>
</div>
<div class="service-card abs" style="left:864px;top:1848px">
  <svg viewBox="0 0 88 100"><use href="#hex"/><rect x="28" y="42" width="32" height="20" rx="3" fill="none" stroke="#fff" stroke-width="2.5"/><path d="M36 42v-5h16v5M28 51h32" fill="none" stroke="#fff" stroke-width="2.5"/></svg>
  <div class="label">Pre-construction<br>Planning</div>
</div>
<div class="service-card abs" style="left:114px;top:2070px">
  <svg viewBox="0 0 88 100"><use href="#hex"/><circle cx="44" cy="44" r="8" fill="none" stroke="#fff" stroke-width="2.5"/><path d="M32 44h24M30 68c2-9 7-12 14-12s12 3 14 12" fill="none" stroke="#fff" stroke-width="2.5"/></svg>
  <div class="label">Value<br>Engineering</div>
</div>
<div class="service-card abs" style="left:364px;top:2070px">
  <svg viewBox="0 0 88 100"><use href="#hex"/><circle cx="44" cy="50" r="17" fill="none" stroke="#fff" stroke-width="2.5"/><path d="M38 58c0-10 6-15 13-16-1 8-5 14-13 16z" fill="none" stroke="#fff" stroke-width="2.5"/></svg>
  <div class="label">Sustainable<br>Construction Practices</div>
</div>
<div class="service-card abs" style="left:614px;top:2070px">
  <svg viewBox="0 0 88 100"><use href="#hex"/><circle cx="44" cy="44" r="10" fill="none" stroke="#fff" stroke-width="2.5"/><path d="M39 44l4 4 6-7M30 66l8-6h12l8 6" fill="none" stroke="#fff" stroke-width="2.5"/></svg>
  <div class="label">Quality Assurance and<br>Control</div>
</div>
<div class="service-card abs" style="left:864px;top:2070px">
  <svg viewBox="0 0 88 100"><use href="#hex"/><rect x="30" y="32" width="28" height="36" rx="2" fill="none" stroke="#fff" stroke-width="2.5"/><path d="M35 40h18M35 48h6M45 48h8M35 56h6M45 56h8M35 62h18" stroke="#fff" stroke-width="2.5"/></svg>
  <div class="label">Project Estimating and<br>Budgeting</div>
</div>
<a class="btn view-all abs">VIEW ALL</a>

<!-- experience -->
<section class="experience abs">
  <h2>Experience</h2>
  <div class="underline"></div>
  <p>With decades of experience, we bring unparalleled expertise to every project we undertake. Our team consists of seasoned professionals who are experts in their respective fields.</p>
</section>

<!-- portfolio -->
<h2 class="heading portfolio-title abs">Portfolio</h2>
<div class="underline portfolio-underline abs"></div>
<div class="shot abs" style="left:0;top:2886px;width:135px;height:219px" role="img" aria-label="Suburban house with double garage"></div>
<div class="shot abs" style="left:0;top:3125px;width:135px;height:295px" role="img" aria-label="Gabled house facade under blue sky"></div>
<div class="shot abs" style="left:152px;top:2945px;width:438px;height:397px" role="img" aria-label="Grey shingle family home with green lawn"></div>
<div class="shot modern abs" style="left:608px;top:2995px;width:438px;height:398px" role="img" aria-label="Modern white house with timber cladding and garage"></div>
<div class="shot abs" style="left:1063px;top:2886px;width:137px;height:219px" role="img" aria-label="Two-storey home with front porch"></div>
<div class="shot abs" style="left:1063px;top:3125px;width:137px;height:295px" role="img" aria-label="White colonial house among trees"></div>
<div class="arrow-btn abs" style="left:532px;top:3437px"><svg width="50" height="50" viewBox="0 0 50 50"><path d="M28 17 20 25l8 8" fill="none" stroke="#232a65" stroke-width="3"/></svg></div>
<div class="arrow-btn abs" style="left:600px;top:3437px"><svg width="50" height="50" viewBox="0 0 50 50"><path d="M22 17l8 8-8 8" fill="none" stroke="#232a65" stroke-width="3"/></svg></div>

<!-- testimonials -->
<svg width="0" height="0" style="position:absolute"><defs><symbol id="star" viewBox="0 0 20 20"><path d="M10 1l2.7 5.8 6.3.7-4.7 4.3 1.3 6.2L10 14.9 4.4 18l1.3-6.2L1 7.5l6.3-.7z" fill="#4fb49a"/></symbol></defs></svg>
<h2 class="heading reviews-title abs">Client Satisfaction</h2>
<div class="underline reviews-underline abs"></div>

<article class="review abs" style="left:36px;top:3725px">
  <div class="stars"><svg width="19" height="19"><use href="#star"/></svg><svg width="19" height="19"><use href="#star"/></svg><svg width="19" height="19"><use href="#star"/></svg><svg width="19" height="19"><use href="#star"/></svg><svg width="19" height="19"><use href="#star"/></svg></div>
  <h3>Volup tatem accus antiu lasei saeioasei camsei</h3>
  <p>Consectetur adipiscing elitsed do eiusmod tempor incididun.</p>
  <div class="reviewer"><span class="avatar"></span><div><b>Mara Ellison</b><span>CEO &amp; Founder</span></div></div>
</article>
<article class="review abs" style="left:324px;top:3725px">
  <div class="stars"><svg width="19" height="19"><use href="#star"/></svg><svg width="19" height="19"><use href="#star"/></svg><svg width="19" height="19"><use href="#star"/></svg><svg width="19" height="19"><use href="#star"/></svg><svg width="19" height="19"><use href="#star"/></svg></div>
  <h3>Volup tatem accus antiu lasei saeioasei camsei</h3>
  <p>Consectetur adipiscing elit, sed do eiusmod tempor incididunt ut labore et dolore magna.</p>
  <div class="reviewer"><span class="avatar"></span><div><b>Mara Ellison</b><span>CEO &amp; Founder</span></div></div>
</article>
<article class="review abs" style="left:612px;top:3725px">
  <div class="stars"><svg width="19" height="19"><use href="#star"/></svg><svg width="19" height="19"><use href="#star"/></svg><svg width="19" height="19"><use href="#star"/></svg><svg width="19" height="19"><use href="#star"/></svg><svg width="19" height="19"><use href="#star"/></svg></div>
  <h3>Volup tatem accus antiu lasei saeioasei camsei</h3>
  <p>Hansectetur adipiscing elit, sed do eiusmod tempor incididunt ut labore et dolore magna aliqua. Ut enim aliquip ex ea commodo consequ.</p>
  <div class="reviewer"><span class="avatar"></span><div><b>Mara Ellison</b><span>CEO &amp; Founder</span></div></div>
</article>
<article class="review abs" style="left:900px;top:3725px">
  <div class="stars"><svg width="19" height="19"><use href="#star"/></svg><svg width="19" height="19"><use href="#star"/></svg><svg width="19" height="19"><use href="#star"/></svg><svg width="19" height="19"><use href="#star"/></svg><svg width="19" height="19"><use href="#star"/></svg></div>
  <h3>Volup tatem accus antiu lasei saeioasei camsei</h3>
  <p>Consectetur adipiscing elitsed do eiusmod tempor incididun.</p>
  <div class="reviewer"><span class="avatar"></span><div><b>Mara Ellison</b><span>CEO &amp; Founder</span></div></div>
</article>
<div class="dots review-dots abs"><span class="dot"></span><span class="dot on"></span><span class="dot"></span><span class="dot"></span></div>

<!-- footer -->
<svg class="footer-curve abs" viewBox="0 0 1200 140" preserveAspectRatio="none">
  <path d="M0 0 Q600 200 1200 0 V140 H0Z" fill="#232a65"/>
  <path d="M0 16 Q600 228 1200 16 V140 H0Z" fill="#1d1d1f"/>
</svg>
<footer class="site-footer abs"></footer>
<div class="footer-brand abs">Keystone Ridge<br>Construction LLC</div>
<span class="social abs" style="left:245px"></span>
<span class="social abs" style="left:291px"></span>

<div class="footer-col abs" style="left:465px;top:4418px">
  <h4>Quick Links</h4><div class="underline"></div>
  <a>Home</a><a>About</a><a>Services</a><a>Projects</a><a>Contact Us</a>
</div>
<div class="footer-col abs" style="left:677px;top:4418px">
  <h4>Links</h4><div class="underline"></div>
  <a>Copyright</a><a>Legal</a><a>Privacy</a><a>Accessibility</a><a>Sitemap</a>
</div>
<div class="footer-col abs" style="left:880px;top:4418px">
  <h4>Support</h4><div class="underline"></div>
  <a>Team</a><a>About Us</a><a>Careers</a><a>Our Values</a>
</div>
<div class="footer-rule abs"></div>
<div class="copyright abs">©2024. All rights reserved.</div>
<div class="legal abs"><span>Privacy</span><span>|</span><span>Terms &amp; Conditions</span></div>

</body>
</html>
```